Birch Kettle Coffee Needs A New Bag Label

We require a redesign of our coffee bag label. Our company, Birch Kettle Coffee roasts and packages Fair Trade Organic Coffee in 5 lb and 1 lb bags hot from the roaster. Our company aligns itself with a Canadian outdoor lifestyle involving hiking, camping, canoeing, mountain biking etc. I am attaching our existing logo which is based on a "tent sign" used to indicate a campsite. I'm also attaching our company logo, which is based on a "Camp Patch" that is common for summer camps. The label needs to have "blank space" where I can change the name and description of the different coffees/blends. We use black coffee bags. We are looking for a label that is more upscale from what we currently have.
Target Market(s)
People who love coffee and enjoy outdoor activities. Camping, hiking, climbing, canoeing, sailing etc.
Industry/Entity Type
Coffee Shop
Requirements
Must have
- Project must have an editable space where we can change the name of the coffee (ie Nicaragua, Guatemala, French Roast) and a space where we can edit the descriptions (ie : Dark Roast, Full Body, Citrus Aroma etc)
- I am including a sample of our existing label. The triangle symbol is based on a symbol used to make a camp site. I am also including our logo which is based on a camp patch common at many summer camps in North America.
- The label must be 3" wide by 4" high
Should not have
- Must not be too busy.

```html
<!DOCTYPE html>
<html lang="en">
<head>
<meta charset="utf-8">
<title>Birch Kettle Coffee – Colombia Label</title>
<link href="https://fonts.googleapis.com/css2?family=Comfortaa:wght@500&family=Kurale&family=Oswald:wght@400&display=swap" rel="stylesheet">
<style>
  :root {
    --kraft: #e8cdaf;
    --ink: #46414f;
    --cream: #ecd2b3;
    --saucer: #c9c9c9;
    --rim: #f2f2f2;
    --shadow: #c8ae93;
    --brew: #4a2616;
  }
  html, body {
    margin: 0;
    padding: 0;
    width: 900px;
    height: 1200px;
    overflow: hidden;
    background: var(--kraft);
  }
  .label {
    position: relative;
    width: 900px;
    height: 1200px;
    background: var(--kraft);
    color: var(--ink);
  }
  .frame {
    position: absolute;
    inset: 0;
  }
  .brand-plate {
    position: absolute;
    left: 204px;
    top: 0;
    width: 486px;
    height: 256px;
    background: var(--ink);
    box-shadow: 0 0 0 10px var(--kraft), 0 0 0 14px var(--ink);
    display: flex;
    flex-direction: column;
    align-items: center;
    justify-content: center;
    gap: 12px;
    font-family: "Comfortaa", sans-serif;
    font-weight: 500;
    color: var(--cream);
  }
  .brand-plate .brand-name {
    font-size: 54px;
    letter-spacing: 1px;
    line-height: 1;
  }
  .brand-plate .brand-sub {
    font-size: 46px;
    line-height: 1;
    display: flex;
    align-items: center;
    gap: 20px;
  }
  .brand-plate .brand-sub::before,
  .brand-plate .brand-sub::after {
    content: "";
    width: 30px;
    height: 4px;
    background: var(--cream);
  }
  .brand-badge {
    position: absolute;
    left: 716px;
    top: 160px;
    width: 150px;
    display: flex;
    flex-direction: column;
    align-items: center;
    gap: 10px;
    text-align: center;
    font-family: "Kurale", serif;
    font-size: 23px;
    line-height: 1.15;
    color: var(--ink);
  }
  .brand-badge .dot {
    width: 40px;
    height: 40px;
    border-radius: 50%;
    background: var(--ink);
  }
  .origin {
    position: absolute;
    left: 0;
    width: 900px;
    top: 348px;
    text-align: center;
    font-family: "Kurale", serif;
    font-size: 50px;
    letter-spacing: 2px;
    margin: 0;
    font-weight: 400;
  }
  .cup-art {
    position: absolute;
    left: 254px;
    top: 460px;
    width: 390px;
    height: 390px;
    border-radius: 50%;
    background: radial-gradient(circle closest-side at 50% 50%, var(--brew) 0 64%, var(--rim) 65% 76%, var(--saucer) 77% 100%);
    box-shadow: 22px 22px 0 var(--shadow);
  }
  .divider {
    position: absolute;
    left: 70px;
    top: 884px;
    width: 760px;
    height: 4px;
    background: var(--ink);
  }
  .specs {
    position: absolute;
    left: 0;
    top: 900px;
    width: 900px;
    height: 210px;
    display: grid;
    grid-template-columns: 296px 324px 280px;
  }
  .spec {
    text-align: center;
    padding-top: 16px;
  }
  .spec + .spec {
    border-left: 4px dotted var(--ink);
  }
  .spec h2 {
    margin: 0 0 24px;
    font-family: "Oswald", sans-serif;
    font-weight: 400;
    font-size: 38px;
    letter-spacing: 1px;
    line-height: 1;
  }
  .spec p {
    margin: 0;
    font-family: "Kurale", serif;
    font-size: 31px;
    line-height: 1.55;
    letter-spacing: 1px;
  }
</style>
</head>
<body>
  <div class="label">
    <svg class="frame" width="900" height="1200" viewBox="0 0 900 1200" aria-hidden="true">
      <g fill="none" stroke="#46414f" stroke-width="5">
        <polyline points="190,30 24,30 24,1176 876,1176 876,30 706,30"/>
      </g>
    </svg>

    <header class="brand-plate">
      <span class="brand-name">Birch Kettle</span>
      <span class="brand-sub">Coffee</span>
    </header>

    <div class="brand-badge">
      <span class="dot"></span>
      <span>Birch Kettle<br>Coffee</span>
    </div>

    <h1 class="origin">Colombia</h1>

    <div class="cup-art" role="img" aria-label="Top view of a cup of black coffee on a saucer, marked with the camp tent symbol"></div>

    <div class="divider"></div>

    <section class="specs">
      <div class="spec">
        <h2>VARIETY:</h2>
        <p>Medium<br>Dark</p>
      </div>
      <div class="spec">
        <h2>FLAVOUR:</h2>
        <p>Toasty Sweet<br>with Dried<br>Red Fruit</p>
      </div>
      <div class="spec">
        <h2>NET WT.</h2>
        <p>450 g</p>
      </div>
    </section>
  </div>
</body>
</html>
```